KRM/DOLV JV

We need a business card design for a joint venture construction company. We have two logos that need to appear and need to be cleaned up. We are looking for a simple design with a white background and black lettering. The company name is K. Marlowitz, Inc./D. Olvera Construction Corp. J.V.

The website is www.krmdolv.com

Please indicate spaces for phone; fax and cell. For this mockup use the following info:

Rob Kessing
Project Enginner
2817 Route 4
Castleton, NY 12987
robkrmdolv@mailbrook.com
Office: 555-014-38826
Fax: 555-014-6190
Cell: 555-019-4473

Please note; the logos themselves should not include the company names but the card should include the name of the company - K. Marlowitz, Inc./D. Olvera Construction Corp., J.V. 

Also, the logo should appear alphabetically KRM first, then DOLV, but they should be the same size.

Industry/Entity Type

Construction

Requirements
Should not have
• The logos should not include the company name; please crop that from the image.

```html
<!DOCTYPE html>
<html lang="en">
<head>
<meta charset="utf-8">
<title>KRM/DOLV JV – Business Card</title>
<link rel="stylesheet" href="https://fonts.googleapis.com/css2?family=Archivo:wght@400;600;700&display=swap">
<style>
  :root {
    --page: #e9ecee;
    --card: #ffffff;
    --ink: #1e1e1e;
    --ink-soft: #4a4a4a;
    --band: #bdbdbd;
    --badge: #c9c9c9;
  }
  * { box-sizing: border-box; margin: 0; padding: 0; }
  html, body { width: 1200px; height: 1080px; overflow: hidden; }
  body {
    background: var(--page);
    font-family: "Archivo", Arial, sans-serif;
    color: var(--ink);
    position: relative;
  }
  .card {
    position: absolute;
    left: 100px; top: 254px;
    width: 1000px; height: 572px;
    background: var(--card);
    box-shadow: 0 10px 30px rgba(0,0,0,.18);
    overflow: hidden;
  }
  .brand-badge {
    position: absolute;
    display: flex; align-items: center; justify-content: center;
    width: 104px; height: 104px;
    border-radius: 50%;
    background: var(--badge);
    font-weight: 700; font-size: 26px; letter-spacing: 1px;
    color: var(--ink);
  }
  .brand-badge--krm { right: 46px; top: 30px; }
  .brand-badge--dolv { left: 44px; top: 120px; }
  .company-name {
    position: absolute;
    left: 170px; top: 126px;
    font-weight: 700; font-size: 28px; line-height: 1.5;
    letter-spacing: .5px;
  }
  .company-name span { display: block; }
  .company-name .line-1 { padding-left: 130px; }
  .band {
    position: absolute; left: 0; width: 100%;
    background: var(--band);
  }
  .band--name { top: 250px; height: 96px; }
  .person {
    position: absolute; left: 330px; top: 262px;
    font-size: 22px; line-height: 1.45;
  }
  .person .name { font-weight: 600; font-size: 25px; }
  .person .title { color: var(--ink-soft); }
  .contact {
    position: absolute;
    font-size: 20px; line-height: 1.55;
  }
  .contact li { list-style: none; display: flex; align-items: center; gap: 10px; }
  .contact svg { width: 20px; height: 20px; flex: none; fill: var(--ink); }
  .contact--phones { left: 60px; top: 372px; }
  .contact--location { left: 560px; top: 360px; }
  .contact--location li { align-items: flex-start; margin-bottom: 18px; }
  .contact--location svg { width: 26px; height: 26px; margin-top: 4px; }
  .band--web {
    top: 480px; height: 50px;
    display: flex; align-items: center; justify-content: flex-end;
    padding-right: 120px;
    font-weight: 600; font-size: 21px; letter-spacing: .5px;
    background: transparent;
  }
  .band--web::before {
    content: ""; position: absolute; left: 320px; right: 40px; top: 0; bottom: 0;
    background: var(--band); border-radius: 25px; z-index: -1;
  }
  .band--web { z-index: 1; }
  .footer-strip {
    position: absolute; left: 150px; bottom: 0;
    width: 330px; height: 34px;
    background: var(--band); border-radius: 17px 17px 0 0;
  }
</style>
</head>
<body>
  <article class="card">
    <div class="brand-badge brand-badge--krm">KRM</div>
    <div class="brand-badge brand-badge--dolv">DOLV</div>

    <h1 class="company-name">
      <span class="line-1">K. Marlowitz, Inc./</span>
      <span class="line-2">D. Olvera Construction Corp., J.V.</span>
    </h1>

    <div class="band band--name"></div>
    <div class="person">
      <p class="name">Rob Kessing</p>
      <p class="title">Project Engineer</p>
    </div>

    <ul class="contact contact--phones">
      <li><svg viewBox="0 0 24 24" aria-hidden="true"><path d="M6.6 10.8a15 15 0 0 0 6.6 6.6l2.2-2.2c.3-.3.7-.4 1-.2 1.1.4 2.3.6 3.6.6.6 0 1 .4 1 1V20c0 .6-.4 1-1 1A17 17 0 0 1 3 4c0-.6.4-1 1-1h3.5c.6 0 1 .4 1 1 0 1.3.2 2.5.6 3.6.1.3 0 .7-.2 1z"/></svg>Office: 555-014-38826</li>
      <li><svg viewBox="0 0 24 24" aria-hidden="true"><path d="M6 2h12v6H6zM4 9h16a2 2 0 0 1 2 2v7h-4v4H6v-4H2v-7a2 2 0 0 1 2-2zm4 7v4h8v-4z"/></svg>Fax: 555-014-6190</li>
      <li><svg viewBox="0 0 24 24" aria-hidden="true"><path d="M7 1h10a2 2 0 0 1 2 2v18a2 2 0 0 1-2 2H7a2 2 0 0 1-2-2V3a2 2 0 0 1 2-2zm0 3v14h10V4zm5 15.5a1 1 0 1 0 0 2 1 1 0 0 0 0-2z"/></svg>Cell: 555-019-4473</li>
    </ul>

    <ul class="contact contact--location">
      <li><svg viewBox="0 0 24 24" aria-hidden="true"><path d="M12 2a7 7 0 0 0-7 7c0 5.3 7 13 7 13s7-7.7 7-13a7 7 0 0 0-7-7zm0 9.5A2.5 2.5 0 1 1 12 6.5a2.5 2.5 0 0 1 0 5z"/></svg><span>2817 Route 4<br>Castleton, NY 12987</span></li>
      <li><svg viewBox="0 0 24 24" aria-hidden="true"><path d="M2 5h20v14H2zm2 2v.5l8 5 8-5V7zm0 2.9V17h16V9.9l-8 5z"/></svg><span>robkrmdolv@mailbrook.com</span></li>
    </ul>

    <div class="band band--web">www.krmdolv.com</div>
    <div class="footer-strip"></div>
  </article>
</body>
</html>
```